Fernbrook Plots - Online-only garden installation company

Online-only garden installation company. Our demographic is middle aged / suburban women, and we anticipate Facebook driving traffic to this website, as well as referrals from garden centers. The website must be very simple in design and function.

All orders will be placed through the website, including size of garden (3 options), location in yard, payment, and scheduling of installation date.

The website should employ a 3 step process:

Step 1: Select garden size. Either an 4' X 4', 8' X 4', or 12' X 4'.

Step 2: Select a location. We would like to use google maps to look up a US address, then "drag and drop" one of the garden sizes from step 1 to the location the customer would like us to install the garden at their home.

Step 3: Pick an installation date and pay. Using an online calendar the customer will pick a date, and then pay for the installation via credit card.

The website will be linked to an email account, FernbrookPlots@mailzy.com to inform us of orders placed.

Target Market(s)

Our demographic is middle aged / suburban women, and we anticipate Facebook driving traffic to this website, as well as referrals from garden centers.

Industry/Entity Type

Coding

Number of Pages Required

Requirements
Must have
• Scheduling and payment options.

```html
<!DOCTYPE html>
<html lang="en">
<head>
<meta charset="utf-8">
<title>Fernbrook Plots – A Garden Installation Company</title>
<link rel="stylesheet" href="https://fonts.googleapis.com/css2?family=Ruda:wght@400;700&family=Open+Sans:wght@400;600&display=swap">
<style>
:root{
  --green:#3b7d33;
  --green-dark:#2f6a29;
  --orange:#e2612a;
  --ink:#333333;
  --muted:#888888;
  --line:#d9d9d9;
  --paper:#ffffff;
  --mist:#efefef;
}
*{box-sizing:border-box;margin:0;padding:0}
html,body{width:1200px;height:3564px;overflow:hidden;background:var(--paper)}
body{position:relative;font-family:"Ruda",sans-serif;color:var(--ink)}

/* header */
.site-header{position:absolute;left:0;top:0;width:1200px;height:202px}
.contact{position:absolute;top:108px;display:flex;align-items:center;gap:14px;font-size:24px;color:var(--ink)}
.contact--phone{left:200px}
.contact--mail{left:748px}
.brand{position:absolute;left:450px;top:40px;width:300px;text-align:center;color:var(--green-dark);font-weight:700;font-size:30px;line-height:34px;letter-spacing:2px}
.brand__mark{display:block;width:34px;height:34px;border-radius:50%;background:var(--orange);margin:0 auto 8px}

.main-nav{position:absolute;left:0;top:202px;width:1200px;height:60px;background:var(--green);display:flex;justify-content:center;align-items:center}
.main-nav a{color:#fff;text-decoration:none;font-size:17px;letter-spacing:.5px;padding:0 36px}

/* hero */
.hero{position:absolute;left:0;top:262px;width:1200px;height:503px;background:linear-gradient(160deg,#4a3322 0%,#7a4a2a 40%,#c0652a 60%,#5c3b25 100%)}
.hero__title{position:absolute;left:0;top:230px;width:1200px;text-align:center;color:#fff;font-size:31px;letter-spacing:1px}
.hero__dots{position:absolute;left:586px;top:458px;display:flex;gap:8px}
.hero__dots span{width:9px;height:9px;border-radius:50%;background:#fff;opacity:.8}

/* process banner */
.process-banner{position:absolute;left:173px;top:805px;width:849px;height:328px;background:linear-gradient(120deg,#6b4224 0%,#a0582a 45%,#d0702e 70%,#7a4a2a 100%)}
.process-banner h2{position:absolute;left:0;top:98px;width:849px;text-align:center;color:#fff;font-size:54px;line-height:62px;font-weight:700;letter-spacing:1px}

/* steps */
.step-icon{position:absolute;left:186px;width:80px;height:80px;border-radius:50%}
.step-num{position:absolute;left:288px;font-size:58px;color:var(--green);line-height:60px}
.step-label{position:absolute;left:349px;font-size:20px;line-height:25px;color:var(--ink);letter-spacing:.5px}
.field{position:absolute;left:190px;width:297px;height:38px;border:1px solid var(--line);display:flex;align-items:center;padding:0 12px;gap:12px;font-size:11px;color:#555;font-family:"Open Sans",sans-serif}
.field__chev{margin-left:auto}
.step-media{position:absolute;left:518px;width:497px;height:271px}
.divider{position:absolute;left:173px;width:849px;border-top:3px dotted #9a9a9a}

.garden-photo{background:linear-gradient(180deg,#5f7a56 0%,#3e7a2a 45%,#69b33a 75%,#80c442 100%)}
.garden-photo span{position:absolute;left:0;top:100px;width:100%;padding-left:140px;text-align:center;color:#fff;font-size:60px}
.map-area{background:linear-gradient(135deg,#e7eee0 0%,#dfe7d5 50%,#c9dcee 100%)}

.calendar{position:absolute;left:518px;top:1951px;width:497px;height:318px;background:#f6f6f6;padding-top:28px}
.calendar h3{text-align:center;font-size:20px;font-weight:400;letter-spacing:1px;margin-bottom:22px}
.calendar table{margin-left:102px;border-collapse:collapse;width:290px}
.calendar th{font-size:12px;font-weight:400;color:var(--green);padding:0 0 12px;text-align:left}
.calendar td{font-size:15px;height:35px;text-align:left;color:var(--ink)}
.calendar td.out{color:#bbb}

/* news */
.news{position:absolute;left:0;top:2359px;width:1200px;height:357px;background:var(--mist)}
.news h2{position:absolute;left:0;top:62px;width:1200px;text-align:center;color:var(--green);font-size:34px;font-weight:400;letter-spacing:1px}
.news-item{position:absolute;top:167px;display:flex;gap:46px}
.news-date{flex:none;width:70px;height:120px;background:var(--orange);color:#fff;text-align:center;padding-top:9px}
.news-date .m{font-size:26px;line-height:30px}
.news-date .d{font-size:23px;line-height:28px;border-bottom:2px solid rgba(255,255,255,.7);margin:0 5px 7px;padding-bottom:2px}
.news-date .y{font-size:18px}
.news-body{width:305px}
.news-body h3{font-size:23px;font-weight:400;line-height:28px;color:var(--ink)}
.news-body p{font-size:13px;color:#555;margin-top:6px;font-family:"Open Sans",sans-serif}

/* testimonials */
.testimonials{position:absolute;left:0;top:2716px;width:1200px;height:458px;background:linear-gradient(90deg,#e9e8e4 0%,#dddcd6 55%,#d9793a 80%,#dcd9d2 100%)}
.quote-card{position:absolute;left:164px;top:114px;width:546px;height:287px;background:#fff;box-shadow:0 6px 14px rgba(0,0,0,.18)}
.quote-card h2{position:absolute;left:38px;top:32px;font-size:34px;font-weight:400;color:var(--green);letter-spacing:.5px}
.quote-nav{position:absolute;right:20px;top:38px;display:flex;gap:12px}
.quote-mark{position:absolute;left:34px;top:100px;font-size:130px;line-height:130px;color:var(--orange);font-family:Georgia,serif}
.quote-card blockquote{position:absolute;left:146px;top:110px;width:370px;font-size:13.5px;line-height:23px;color:#444;font-family:"Open Sans",sans-serif}
.quote-card cite{position:absolute;left:146px;top:240px;font-style:normal;font-weight:700;font-size:18px;color:var(--orange)}

/* footer */
.site-footer{position:absolute;left:0;top:3174px;width:1200px;height:390px}
.site-footer .brand{top:36px}
.social{position:absolute;left:497px;top:194px;display:flex;gap:12px}
.social span{width:34px;height:34px;border-radius:50%;border:2px solid var(--orange)}
.footer-nav{position:absolute;left:0;top:258px;width:1200px;text-align:center;font-size:14px}
.footer-nav a{color:var(--ink);text-decoration:none;padding:0 12px}
.footer-nav i{font-style:normal;color:#777}
.copyright{position:absolute;left:0;top:300px;width:1200px;text-align:center;font-size:13px;letter-spacing:.5px}
</style>
</head>
<body>

<header class="site-header">
  <div class="contact contact--phone">
    <svg width="20" height="20" viewBox="0 0 24 24"><path d="M6.6 10.8c1.4 2.8 3.8 5.1 6.6 6.6l2.2-2.2c.3-.3.7-.4 1-.2 1.1.4 2.3.6 3.6.6.6 0 1 .4 1 1V20c0 .6-.4 1-1 1C10.6 21 3 13.4 3 4c0-.6.4-1 1-1h3.5c.6 0 1 .4 1 1 0 1.3.2 2.5.6 3.6.1.3 0 .7-.2 1z" fill="#e2612a"/></svg>
    <span>1-800-555-0147</span>
  </div>
  <div class="brand"><span class="brand__mark"></span>FERNBROOK<br>PLOTS</div>
  <div class="contact contact--mail">
    <svg width="20" height="16" viewBox="0 0 20 16"><rect x="1" y="1" width="18" height="14" rx="1" fill="none" stroke="#e2612a" stroke-width="2"/><path d="M1 2l9 7 9-7" fill="none" stroke="#e2612a" stroke-width="2"/></svg>
    <span>info@fernbrookplots</span>
  </div>
</header>

<nav class="main-nav">
  <a href="#">HOME</a><a href="#">ABOUT US</a><a href="#">SERVICES</a><a href="#">FAQ'S</a><a href="#">CLIENTS</a><a href="#">CONTACT US</a>
</nav>

<section class="hero" role="img" aria-label="Freshly pulled carrots with green tops lying on garden soil">
  <p class="hero__title">A GARDEN INSTALLATION COMPANY</p>
  <div class="hero__dots"><span></span><span></span></div>
</section>

<section class="process-banner" role="img" aria-label="Carrots, tomatoes and an onion on a wooden board">
  <h2>OUR THREE STEP<br>PROCESS</h2>
</section>

<div class="step-icon" style="top:1225px;background:radial-gradient(circle at 50% 35%,#6fb33c 0 30%,#b0703a 31% 100%)" role="img" aria-label="Seedling in soil icon"></div>
<div class="step-num" style="top:1255px">1</div>
<div class="step-label" style="top:1285px">SELECT<br>GARDEN SIZE</div>
<div class="field" style="top:1385px">
  <span style="width:4px;height:16px;background:var(--orange)"></span><span>4' X 4'</span>
  <svg class="field__chev" width="12" height="8" viewBox="0 0 12 8"><path d="M1 1l5 5 5-5" fill="none" stroke="#666" stroke-width="1.6"/></svg>
</div>
<div class="step-media garden-photo" style="top:1197px" role="img" aria-label="Lawn with stone path and hedges in a backyard"><span>4' X 4'</span></div>

<div class="divider" style="top:1520px"></div>

<div class="step-icon" style="top:1660px;background:radial-gradient(circle at 40% 40%,#5f8a8a 0 60%,#3f6a6a 61% 100%)" role="img" aria-label="Globe with pointing hand icon"></div>
<div class="step-num" style="top:1683px">2</div>
<div class="step-label" style="top:1685px">SELECT A<br>LOCATION</div>
<div class="field" style="top:1763px">
  <svg width="10" height="14" viewBox="0 0 10 14"><path d="M5 0C2.2 0 0 2.2 0 5c0 3.7 5 9 5 9s5-5.3 5-9c0-2.8-2.2-5-5-5zm0 7a2 2 0 110-4 2 2 0 010 4z" fill="#e2612a"/></svg>
  <span>LOCATION</span>
  <svg class="field__chev" width="12" height="8" viewBox="0 0 12 8"><path d="M1 1l5 5 5-5" fill="none" stroke="#666" stroke-width="1.6"/></svg>
</div>
<div class="step-media map-area" style="top:1575px" role="img" aria-label="Map of the United States with location markers"></div>

<div class="divider" style="top:1903px"></div>

<div class="step-icon" style="top:2030px;background:radial-gradient(circle at 60% 60%,#5aaa4a 0 30%,#6f8f8f 31% 100%)" role="img" aria-label="Gear with leaf icon"></div>
<div class="step-num" style="top:2043px">3</div>
<div class="step-label" style="top:2032px">PICK AN<br>INSTALLATION<br>DATE AND PAY</div>
<div class="field" style="top:2153px">
  <svg width="12" height="12" viewBox="0 0 12 12"><rect x="1" y="2" width="10" height="9" fill="none" stroke="#e2612a" stroke-width="1.4"/><path d="M1 5h10M4 0v3M8 0v3" stroke="#e2612a" stroke-width="1.4"/></svg>
  <span>CALENDAR</span>
</div>
<div class="calendar">
  <h3>JANUARY</h3>
  <table>
    <tr><th>SUN</th><th>MON</th><th>TUE</th><th>WED</th><th>THU</th><th>FRI</th><th>SAT</th></tr>
    <tr><td class="out">28</td><td class="out">29</td><td class="out">30</td><td class="out">31</td><td>1</td><td>2</td><td>3</td></tr>
    <tr><td>4</td><td>5</td><td>6</td><td>7</td><td>8</td><td>9</td><td>10</td></tr>
    <tr><td>11</td><td>12</td><td>13</td><td>14</td><td>15</td><td>16</td><td>17</td></tr>
    <tr><td>18</td><td>19</td><td>20</td><td>21</td><td>22</td><td>23</td><td>24</td></tr>
    <tr><td>25</td><td>26</td><td>27</td><td>28</td><td>29</td><td>30</td><td class="out">1</td></tr>
  </table>
</div>

<section class="news">
  <h2>RECENT NEWS</h2>
  <article class="news-item" style="left:171px">
    <div class="news-date"><div class="m">DEC</div><div class="d">13TH</div><div class="y">2017</div></div>
    <div class="news-body"><h3>At vero eos et accusam iusto odio dignissimos ducimus qui blanditiis</h3><p>molestias excepturi sint occaecati</p></div>
  </article>
  <article class="news-item" style="left:611px">
    <div class="news-date"><div class="m">DEC</div><div class="d">13TH</div><div class="y">2017</div></div>
    <div class="news-body"><h3>At vero eos et accusa iusto odio dignissimos ducimus qui blanditiis</h3><p>molestias excepturi sint occaecati</p></div>
  </article>
</section>

<section class="testimonials" role="img" aria-label="Bunch of carrots on a white wooden table">
  <div class="quote-card">
    <h2>TESTIMONIALS</h2>
    <div class="quote-nav">
      <svg width="10" height="16" viewBox="0 0 10 16"><path d="M8 1L2 8l6 7" fill="none" stroke="#777" stroke-width="2"/></svg>
      <svg width="10" height="16" viewBox="0 0 10 16"><path d="M2 1l6 7-6 7" fill="none" stroke="#777" stroke-width="2"/></svg>
    </div>
    <div class="quote-mark">&ldquo;</div>
    <blockquote>At vero eos et accusamus et iusto odio dignissimos ducimus qui blanditiis praesentium voluptatum deleniti atque corrupti quos dolores et quas molestias excepturi sint occaecati cupiditate non provident, similique sunt in culpa qui officia deserunt mollitia animi</blockquote>
    <cite>Dana Whitfield</cite>
  </div>
</section>

<footer class="site-footer">
  <div class="brand"><span class="brand__mark"></span>FERNBROOK<br>PLOTS</div>
  <div class="social"><span></span><span></span><span></span><span></span><span></span></div>
  <nav class="footer-nav">
    <a href="#">HOME</a><i>|</i><a href="#">ABOUT US</a><i>|</i><a href="#">SERVICES</a><i>|</i><a href="#">FAQ'S</a><i>|</i><a href="#">CLIENTS</a><i>|</i><a href="#">CONTACT US</a>
  </nav>
  <p class="copyright">© 2017 COMPANY NAME | ALL RIGHTS RESERVED</p>
</footer>

</body>
</html>
```